Business Card Design

Carl Brennow Insurance Agency, an Independent Insurance Agency which was stated on Pellham Row in Laplace, Louisiana on 1958 and has grown the six locations throughout South Louisiana. We sell personal (auto Homeowners flood, liability) and commercial insurance (commercial property, general liability, workers compensation, commercial auto). I am looking for a double sided card with list the five remaining locations on the back or maybe even a folded four sided card. Our home office is a two story building with a green roof. I have had a logo designed which I have attached. Open for revisions but would like to stay with in the same green roof over an M. I have attached the logo but can not tell if I was uploaded.

Target Market(s)

Individual and commercial insurance buyers. Upper income and business owners

Industry/Entity Type

Insurance

Requirements
Must have
• Must have similar logo as uploaded. Green roof over M or something similar. List all location address and phone numbers.

Employee name, office phone number; direct phone line; email address and website list all locations on card. Very Similar colors to current logo.
Nice to have
• Possible folded card with double sided print

```html
<!DOCTYPE html>
<html lang="en">
<head>
<meta charset="utf-8">
<title>Carl Brennow Insurance Agency – Business Card</title>
<link rel="stylesheet" href="https://fonts.googleapis.com/css2?family=Roboto+Condensed:wght@400;700&family=Open+Sans:wght@400;600&display=swap">
<style>
  :root {
    --page-bg: #e9e6e1;
    --card-white: #ffffff;
    --card-grey: #e4e4e4;
    --brand-green: #1b6a4a;
    --brand-blue: #1f6fc0;
    --brand-blue-light: #2a8ad6;
    --brand-blue-dark: #1456a8;
    --ink-grey: #6b7a74;
    --ink-white: #ffffff;
  }
  * { box-sizing: border-box; margin: 0; padding: 0; }
  html, body { width: 1200px; height: 858px; overflow: hidden; }
  body {
    background: var(--page-bg);
    font-family: "Open Sans", Arial, sans-serif;
    display: flex;
    align-items: center;
    justify-content: center;
    gap: 40px;
  }
  .card {
    width: 540px;
    height: 309px;
    position: relative;
    overflow: hidden;
    box-shadow: 0 6px 18px rgba(0,0,0,0.18);
  }

  /* Front */
  .card--front { background: var(--card-white); }
  .front__brand {
    position: absolute;
    left: 0; top: 0; right: 0;
    height: 150px;
    display: flex;
    align-items: center;
    justify-content: center;
  }
  .front__band {
    position: absolute;
    left: 0; right: 0;
    top: 150px;
    height: 38px;
    background: var(--brand-green);
  }
  .front__panel {
    position: absolute;
    left: 0; right: 0;
    top: 188px; bottom: 0;
    background: linear-gradient(100deg, var(--brand-blue-dark) 0%, var(--brand-blue) 55%, var(--brand-blue-light) 100%);
  }
  .employee {
    position: absolute;
    left: 34px;
    top: 156px;
    color: var(--ink-white);
    font-family: "Roboto Condensed", Arial, sans-serif;
  }
  .employee__name { font-weight: 700; font-size: 22px; letter-spacing: 0.3px; line-height: 26px; }
  .employee__title { font-weight: 400; font-size: 17px; line-height: 24px; margin-top: 8px; margin-left: 40px; }
  .contacts {
    position: absolute;
    left: 250px;
    top: 200px;
    list-style: none;
    color: var(--ink-white);
    font-family: "Roboto Condensed", Arial, sans-serif;
    font-size: 17px;
    line-height: 24px;
  }
  .contacts li { display: flex; align-items: center; gap: 9px; }
  .contacts svg { width: 13px; height: 13px; flex: none; }

  /* Brand lockup (shared) */
  .brand { display: flex; align-items: center; gap: 14px; }
  .brand__mark { width: 40px; height: 40px; background: var(--brand-green); flex: none; }
  .brand__text { display: flex; flex-direction: column; }
  .brand__name {
    font-family: "Roboto Condensed", Arial, sans-serif;
    font-weight: 700;
    color: var(--brand-green);
    text-transform: uppercase;
    font-size: 28px;
    line-height: 30px;
    letter-spacing: 0.2px;
  }
  .brand__tagline {
    font-family: "Roboto Condensed", Arial, sans-serif;
    font-weight: 700;
    color: var(--ink-grey);
    font-size: 16px;
    line-height: 20px;
    margin-top: 2px;
  }
  .brand__locations {
    font-family: "Open Sans", Arial, sans-serif;
    font-weight: 600;
    color: var(--brand-green);
    font-size: 8.5px;
    letter-spacing: 0.4px;
    margin-top: 6px;
  }

  /* Back */
  .card--back {
    background: linear-gradient(135deg, var(--card-white) 0%, var(--card-grey) 100%);
    display: flex;
    align-items: center;
    justify-content: center;
  }
  .card--back .brand__name { font-size: 31px; line-height: 33px; }
</style>
</head>
<body>

  <section class="card card--front" aria-label="Business card front">
    <div class="front__brand">
      <div class="brand">
        <span class="brand__mark" aria-hidden="true"></span>
        <div class="brand__text">
          <span class="brand__name">Carl Brennow<br>Insurance Agency</span>
          <span class="brand__tagline">Serving Pellham Row Since 1961</span>
          <span class="brand__locations">Ashford • Belmont • Corley • Dunmore • Eastvale • Fairbrook</span>
        </div>
      </div>
    </div>
    <div class="front__band"></div>
    <div class="front__panel"></div>
    <div class="employee">
      <p class="employee__name">EMPLOYEE NAME</p>
      <p class="employee__title">Your Title</p>
    </div>
    <ul class="contacts">
      <li>
        <svg viewBox="0 0 16 16" aria-hidden="true"><rect x="1" y="6" width="14" height="9" rx="2" fill="#fff"/><path d="M2 6 C2 1 14 1 14 6" stroke="#fff" stroke-width="2" fill="none"/><circle cx="8" cy="10.5" r="2" fill="#1f6fc0"/></svg>
        <span>xxx xxxx xxxx</span>
      </li>
      <li>
        <svg viewBox="0 0 16 16" aria-hidden="true"><path d="M4 1 L7 4 L5 6 C6 9 7 10 10 11 L12 9 L15 12 L12 15 C6 14 2 10 1 4 Z" fill="#fff"/></svg>
        <span>xxx xxxx xxxx</span>
      </li>
      <li>
        <svg viewBox="0 0 16 16" aria-hidden="true"><rect x="1" y="3" width="14" height="10" fill="#fff"/><path d="M1 3 L8 9 L15 3" stroke="#1f6fc0" stroke-width="1.4" fill="none"/></svg>
        <span>info@youremail.com</span>
      </li>
      <li>
        <svg viewBox="0 0 16 16" aria-hidden="true"><circle cx="8" cy="8" r="7" fill="#fff"/><path d="M1 8 H15 M8 1 C4 5 4 11 8 15 M8 1 C12 5 12 11 8 15" stroke="#1f6fc0" stroke-width="1" fill="none"/></svg>
        <span>www.yourwebsite.com</span>
      </li>
    </ul>
  </section>

  <section class="card card--back" aria-label="Business card back">
    <div class="brand">
      <span class="brand__mark" aria-hidden="true"></span>
      <div class="brand__text">
        <span class="brand__name">Carl Brennow<br>Insurance Agency</span>
        <span class="brand__tagline">Serving Pellham Row Since 1961</span>
        <span class="brand__locations">Ashford • Belmont • Corley • Dunmore • Eastvale • Fairbrook</span>
      </div>
    </div>
  </section>

</body>
</html>
```